Business Management System Providor Needs Upscale Business Card Design

We provide an online Claims Management System to the Insurance Industry called Meridel Casework Suite. Although our core offering is claims management, our system provides full business management features including reporting, invoicing, business trend analysis, etc..
We have a worldwide client base and our system has become known for its reliability, rich feature set, and intuitive design. This being the case we would like our cards to maintain a high level of professionalism. We have a tendency to lean toward a corporate look and feel and we would like to maintain that image.
Current Site: www.merideldesk-example.com
Target Market(s)
Big Business, Insurance Professionals, Corporate Organizations
Industry/Entity Type
Business Management
Look and feel
Each slider illustrates characteristics of the customer's brand and the style your logo design should communicate.

```html
<!DOCTYPE html>
<html lang="en">
<head>
<meta charset="utf-8">
<title>Meridel Casework Suite – Business Card</title>
<link href="https://fonts.googleapis.com/css2?family=Open+Sans:wght@300;400;600;700&display=swap" rel="stylesheet">
<style>
  :root {
    --bg: #e9e7e3;
    --card-white: #f7f8f9;
    --brand-blue: #1f4f8e;
    --brand-blue-deep: #143a6d;
    --brand-blue-light: #2f66a8;
    --panel-grey: #c4c7cb;
    --panel-grey-light: #d6d8db;
    --text-grey: #8b9097;
    --white: #ffffff;
  }
  * { box-sizing: border-box; margin: 0; padding: 0; }
  html, body { width: 1200px; height: 1023px; overflow: hidden; }
  body {
    background: var(--bg);
    font-family: "Open Sans", Arial, sans-serif;
    position: relative;
  }
  .card {
    position: absolute;
    width: 640px;
    height: 366px;
    border-radius: 6px;
    box-shadow: 0 8px 24px rgba(0,0,0,0.18);
    overflow: hidden;
  }

  /* Front */
  .card-front { left: 50px; top: 80px; background: var(--card-white); }
  .brand { position: absolute; left: 30px; top: 32px; display: flex; align-items: flex-start; gap: 12px; }
  .brand-square { width: 50px; height: 50px; background: var(--brand-blue); border-radius: 6px; }
  .brand-name { color: var(--brand-blue); font-weight: 700; font-size: 21px; line-height: 22px; }
  .tagline { position: absolute; left: 30px; top: 106px; color: var(--text-grey); font-size: 16px; font-weight: 300; }
  .person { position: absolute; right: 30px; top: 34px; text-align: right; color: var(--brand-blue); }
  .person-name { font-size: 27px; font-weight: 300; letter-spacing: 1px; }
  .person-title { font-size: 13px; font-weight: 400; margin-top: 2px; }
  .contact-panel {
    position: absolute; left: 20px; right: 20px; top: 152px; height: 160px;
    background: var(--panel-grey); border-radius: 10px; overflow: hidden;
    display: grid; grid-template-columns: 1fr 1fr; grid-template-rows: 1fr 1fr;
  }
  .contact { display: flex; align-items: center; gap: 10px; padding: 0 18px; font-size: 14px; white-space: nowrap; }
  .contact.is-blue { background: linear-gradient(180deg, var(--brand-blue-light), var(--brand-blue)); color: var(--white); }
  .contact.is-grey { background: var(--panel-grey-light); color: var(--white); }
  .contact.is-grey-dark { background: var(--panel-grey); color: var(--white); }
  .contact-icon { width: 26px; height: 26px; flex: none; }
  .address {
    position: absolute; left: 0; right: 0; bottom: 20px; text-align: center;
    color: var(--brand-blue); font-size: 11.5px; letter-spacing: 0.6px; text-transform: uppercase;
  }

  /* Back */
  .card-back {
    left: 510px; top: 590px;
    background: linear-gradient(160deg, var(--brand-blue-light) 0%, var(--brand-blue) 45%, var(--brand-blue-deep) 100%);
  }
  .back-brand { position: absolute; right: 46px; bottom: 58px; display: flex; align-items: flex-start; gap: 16px; }
  .back-square { width: 64px; height: 64px; background: rgba(255,255,255,0.9); border-radius: 8px; margin-top: 6px; }
  .back-name { color: var(--white); font-weight: 700; font-size: 40px; line-height: 42px; }
  .back-tagline { color: var(--white); font-size: 17px; font-weight: 400; margin-top: 8px; }
</style>
</head>
<body>

<section class="card card-front" aria-label="Business card front">
  <div class="brand">
    <div class="brand-square"></div>
    <div class="brand-name">Meridel<br>Casework<br>Suite</div>
  </div>
  <div class="tagline">claim management systems</div>

  <div class="person">
    <div class="person-name">DANA WHITCOMBE</div>
    <div class="person-title">Director of Software Development</div>
  </div>

  <div class="contact-panel">
    <div class="contact is-blue">
      <svg class="contact-icon" viewBox="0 0 26 26" aria-hidden="true">
        <circle cx="13" cy="13" r="12" fill="#ffffff" opacity="0.9"/>
        <path d="M9 7c1 0 1.6 2.4 1.6 3 0 .8-1 1-1 1.6.4 1.6 2.2 3.4 3.8 3.8.6 0 .8-1 1.6-1 .6 0 3 .6 3 1.6 0 1.2-1.2 2-2.4 2C11 18 8 15 8 9.4 8 8.2 8.4 7 9 7z" fill="#1f4f8e"/>
      </svg>
      <span>555-014-2208 x215</span>
    </div>
    <div class="contact is-grey-dark">
      <svg class="contact-icon" viewBox="0 0 26 26" aria-hidden="true">
        <circle cx="13" cy="13" r="12" fill="#1f4f8e"/>
        <path d="M9 7c1 0 1.6 2.4 1.6 3 0 .8-1 1-1 1.6.4 1.6 2.2 3.4 3.8 3.8.6 0 .8-1 1.6-1 .6 0 3 .6 3 1.6 0 1.2-1.2 2-2.4 2C11 18 8 15 8 9.4 8 8.2 8.4 7 9 7z" fill="#ffffff"/>
      </svg>
      <span>800-555-0147</span>
    </div>
    <div class="contact is-grey">
      <svg class="contact-icon" viewBox="0 0 26 26" aria-hidden="true">
        <circle cx="13" cy="13" r="12" fill="#1f4f8e"/>
        <circle cx="13" cy="13" r="7" fill="none" stroke="#fff" stroke-width="1.4"/>
        <ellipse cx="13" cy="13" rx="3" ry="7" fill="none" stroke="#fff" stroke-width="1.2"/>
        <line x1="6" y1="13" x2="20" y2="13" stroke="#fff" stroke-width="1.2"/>
      </svg>
      <span>www.merideldesk-example.com</span>
    </div>
    <div class="contact is-blue">
      <svg class="contact-icon" viewBox="0 0 26 26" aria-hidden="true">
        <circle cx="13" cy="13" r="12" fill="#ffffff" opacity="0.9"/>
        <rect x="7" y="9" width="12" height="8" fill="none" stroke="#1f4f8e" stroke-width="1.4"/>
        <path d="M7 9l6 5 6-5" fill="none" stroke="#1f4f8e" stroke-width="1.4"/>
      </svg>
      <span>dana@merideldesk-example.com</span>
    </div>
  </div>

  <div class="address">1180 Harlow Crescent East, Suite 400, Brantmoor, ON Canada A1B 2C3</div>
</section>

<section class="card card-back" aria-label="Business card back">
  <div class="back-brand">
    <div class="back-square"></div>
    <div>
      <div class="back-name">Meridel<br>Casework<br>Suite</div>
      <div class="back-tagline">claim management systems</div>
    </div>
  </div>
</section>

</body>
</html>
```